BrewDune Lane.

I want the full logo on one side. And the other side the card if right Ralf the logo the left half orange like the car in the logo color with Lorena J Torvand
Founder and CEO
Email symbol then ltorvand@brewdunelanex.com
Www symbol. Then Brewdunelanex.com
Phone symbol then 555-214-BREW
The very bottom would like Brew Dune Lane is a division of Tumbler Treks. LLC

```html
<!DOCTYPE html>
<html lang="en">
<head>
<meta charset="utf-8">
<title>Brew Dune Lane – Business Card</title>
<link rel="stylesheet" href="https://fonts.googleapis.com/css2?family=Lato:wght@400;700&display=swap">
<style>
  :root {
    --backdrop: #2b2b2b;
    --card: #ffffff;
    --ink: #1f1f1f;
    --orange: #f0902a;
    --orange-deep: #e07b12;
    --red: #e8403a;
    --rule: #8a8a8a;
    --art-top: #f6d9a8;
    --art-bottom: #e99a3a;
  }
  * { box-sizing: border-box; margin: 0; padding: 0; }
  html, body { width: 1200px; height: 1200px; overflow: hidden; }
  body {
    background: var(--backdrop);
    font-family: "Lato", Arial, sans-serif;
    color: var(--ink);
    position: relative;
  }
  .card {
    position: absolute;
    top: 310px;
    height: 594px;
    background: var(--card);
  }
  .card--contact { left: 234px; width: 364px; }
  .card--brand { left: 627px; width: 369px; }

  .illustration {
    position: absolute;
    border-radius: 6px;
    background: linear-gradient(180deg, var(--art-top), var(--art-bottom));
  }
  .card--contact .illustration { left: 68px; top: 132px; width: 228px; height: 108px; }
  .card--brand .illustration { left: 72px; top: 196px; width: 228px; height: 108px; }

  .rule { position: absolute; height: 2px; background: var(--ink); }
  .rule--under-art { left: 18px; right: 14px; top: 240px; }
  .rule--bottom { left: 18px; right: 14px; top: 434px; }

  .contact-name {
    position: absolute; left: 0; right: 0; top: 263px;
    text-align: center;
    font-weight: 700; font-size: 23px;
    color: var(--orange-deep);
    letter-spacing: -0.2px;
  }
  .contact-title {
    position: absolute; left: 0; right: 0; top: 289px;
    text-align: center; font-size: 16.5px;
  }
  .icon-row {
    position: absolute; left: 88px; width: 190px; top: 318px; height: 26px;
    display: flex; align-items: center; gap: 4px;
  }
  .icon-row .line { flex: 1; height: 1px; background: var(--rule); }
  .icon-row svg { width: 24px; height: 24px; display: block; }
  .contact-lines {
    position: absolute; left: 0; right: 0; top: 351px;
    text-align: center; font-size: 16.5px; line-height: 22px;
  }

  .brand-name {
    position: absolute; left: 0; right: 0; top: 312px;
    text-align: center;
    font-weight: 700; font-size: 35px;
    color: var(--ink);
    letter-spacing: 0.3px;
  }
  .brand-rule { position: absolute; left: 26px; right: 30px; top: 361px; height: 2px; background: var(--ink); }
  .division-note {
    position: absolute; left: 0; right: 0; top: 509px;
    text-align: center; font-size: 16.5px; line-height: 21px;
    color: var(--red);
  }
</style>
</head>
<body>
  <section class="card card--contact">
    <div class="illustration" role="img" aria-label="Illustration of an orange station wagon with a surfboard on the roof, bottles in the window and wooden fencing on each side"></div>
    <div class="rule rule--under-art"></div>
    <h1 class="contact-name">LORENA J TORVAND</h1>
    <p class="contact-title">Founder and CEO</p>
    <div class="icon-row">
      <span class="line"></span>
      <svg viewBox="0 0 24 24" aria-label="Phone">
        <circle cx="12" cy="12" r="12" fill="var(--orange)"/>
        <path d="M8 7.5c.6-.6 1.4-.6 1.8 0l1 1.5c.3.5.2 1-.2 1.4l-.6.5c.5 1.2 1.4 2.1 2.6 2.6l.5-.6c.4-.4 1-.5 1.4-.2l1.5 1c.6.4.6 1.2 0 1.8-.8.8-2 1-3.1.5-2.3-1-4-2.7-5-5-.5-1.1-.3-2.3.5-3.1z" fill="#fff"/>
      </svg>
      <svg viewBox="0 0 24 24" aria-label="Email">
        <circle cx="12" cy="12" r="12" fill="var(--orange)"/>
        <rect x="6.5" y="8" width="11" height="8" rx="1" fill="#fff"/>
        <path d="M7 8.6l5 3.9 5-3.9" fill="none" stroke="var(--orange)" stroke-width="1.2"/>
      </svg>
      <svg viewBox="0 0 24 24" aria-label="Website">
        <circle cx="12" cy="12" r="12" fill="var(--orange)"/>
        <circle cx="12" cy="12" r="5.5" fill="none" stroke="#fff" stroke-width="1.4"/>
        <path d="M6.5 12h11M12 6.5c-2 2.8-2 8.2 0 11M12 6.5c2 2.8 2 8.2 0 11" fill="none" stroke="#fff" stroke-width="1.1"/>
      </svg>
      <span class="line"></span>
    </div>
    <div class="contact-lines">
      <p>555-214-BREW</p>
      <p>ltorvand@brewdunelanex.com</p>
      <p>www.brewdunelanex.com</p>
    </div>
    <div class="rule rule--bottom"></div>
  </section>

  <section class="card card--brand">
    <div class="illustration" role="img" aria-label="Illustration of an orange station wagon with a surfboard on the roof, bottles in the window and wooden fencing on each side"></div>
    <h2 class="brand-name">BREW DUNE LANE</h2>
    <div class="brand-rule"></div>
    <p class="division-note">BREW DUNE LANE IS A DIVISION<br>OF TUMBLER TREKS. LLC</p>
  </section>
</body>
</html>
```